Simple Business Card Design

Professional/clean business card with custom logo included in layout.

Target Market(s)

N/A

Industry/Entity Type

Business

Contact Information for Business Card

Name: Marlene Hoskin, PT; NV Medicaid Provider; Phone: (775) 918-2467; Toll-free phone: (877) 406-1953; email: mar@copperfieldlaneventuresltd.example

Font styles to use
Serif
Decorative
Script

Requirements
Must have
• See "details" above.
Nice to have
• Would be interested to see dark vs. light/grayscale backgrounds that accentuate/contrast the logo colors. (I.e. dark navy background w/ white or grey text, etc.)

```html
<!DOCTYPE html>
<html lang="en">
<head>
<meta charset="utf-8">
<title>Copperfield Lane Ventures – Business Card</title>
<link rel="stylesheet" href="https://fonts.googleapis.com/css2?family=Cinzel:wght@500&family=Open+Sans:wght@400&display=swap">
<style>
  :root {
    --backdrop: #ecebe8;
    --card-white: #ffffff;
    --card-grey: #858585;
    --navy: #222e3c;
    --text-light: #ffffff;
    --logo-grey: #6f7173;
    --logo-light: #d9dadb;
  }
  * { box-sizing: border-box; margin: 0; padding: 0; }
  html, body {
    width: 1190px; height: 1200px; overflow: hidden;
    background: var(--backdrop);
  }
  .canvas { position: relative; width: 1190px; height: 1200px; }

  .card { position: absolute; width: 882px; height: 529px; overflow: hidden; }

  /* Front */
  .card-front { left: 53px; top: 60px; display: flex; }
  .front-brand {
    width: 438px; height: 100%; background: var(--card-white);
    display: flex; align-items: center; justify-content: center;
  }
  .front-details {
    position: relative; flex: 1; height: 100%; background: var(--card-grey);
  }
  .name-banner {
    position: absolute; left: -10px; top: 145px; width: 454px; height: 90px;
    background: var(--navy);
    clip-path: polygon(0 12%, 10px 0, 100% 0, 100% 100%, 10px 100%, 0 88%);
    padding: 14px 0 0 32px; color: var(--text-light);
    font-family: "Cinzel", serif; font-weight: 500;
  }
  .person-name { font-size: 27px; letter-spacing: 0.5px; line-height: 1.2; }
  .person-role { font-size: 18px; margin: 6px 0 0 26px; letter-spacing: 0.3px; }

  .contact-list {
    position: absolute; left: 22px; top: 280px; list-style: none;
    font-family: "Open Sans", sans-serif; font-size: 17.5px; color: var(--text-light);
  }
  .contact-list li { display: flex; align-items: center; height: 38px; }
  .contact-list svg { width: 16px; height: 16px; margin-right: 8px; flex: none; }

  /* Brand name block */
  .brand { display: flex; align-items: center; gap: 16px; }
  .brand-dot { border-radius: 50%; background: var(--logo-grey); flex: none; }
  .brand-name {
    font-family: "Cinzel", serif; font-weight: 500; line-height: 1.15;
    text-align: center;
  }
  .front-brand .brand-dot { width: 34px; height: 34px; }
  .front-brand .brand-name { font-size: 27px; color: var(--logo-grey); }

  /* Back */
  .card-back {
    left: 246px; top: 622px; background: var(--navy);
    display: flex; align-items: center; justify-content: center;
  }
  .card-back .brand-dot { width: 52px; height: 52px; background: var(--logo-light); }
  .card-back .brand-name { font-size: 42px; color: var(--logo-light); }
</style>
</head>
<body>
<main class="canvas">

  <section class="card card-front">
    <div class="front-brand">
      <div class="brand">
        <span class="brand-dot"></span>
        <p class="brand-name">Copperfield Lane<br>Ventures, Ltd.</p>
      </div>
    </div>

    <div class="front-details">
      <div class="name-banner">
        <p class="person-name">Marlene Hoskin, PT</p>
        <p class="person-role">NV Medicaid Provider</p>
      </div>

      <ul class="contact-list">
        <li>
          <svg viewBox="0 0 16 16" aria-hidden="true"><circle cx="8" cy="8" r="7" fill="none" stroke="currentColor" stroke-width="1.3"/><path d="M5.2 4.2l1.6 0 .6 2-1 .8a5 5 0 0 0 2 2l.8-1 2 .6v1.6c-3.6.4-6.4-2.4-6-6z" fill="currentColor"/></svg>
          (877) 406-1953 (TF)
        </li>
        <li>
          <svg viewBox="0 0 16 16" aria-hidden="true"><circle cx="8" cy="8" r="7" fill="none" stroke="currentColor" stroke-width="1.3"/><path d="M5.2 4.2l1.6 0 .6 2-1 .8a5 5 0 0 0 2 2l.8-1 2 .6v1.6c-3.6.4-6.4-2.4-6-6z" fill="currentColor"/></svg>
          (775) 918-2467
        </li>
        <li>
          <svg viewBox="0 0 16 16" aria-hidden="true"><rect x="1.5" y="3.5" width="13" height="9" rx="1" fill="none" stroke="currentColor" stroke-width="1.4"/><path d="M1.5 4l6.5 5 6.5-5" fill="none" stroke="currentColor" stroke-width="1.4"/></svg>
          mar@copperfieldlaneventuresltd.example
        </li>
      </ul>
    </div>
  </section>

  <section class="card card-back">
    <div class="brand">
      <span class="brand-dot"></span>
      <p class="brand-name">Copperfield Lane<br>Ventures, Ltd.</p>
    </div>
  </section>

</main>
</body>
</html>
```